ONE PAGE WEB DESIGN NEEDED for Finance Company

We need a web design (ONE PAGE DESIGN ONLY) for a new finance website called Brightwell Lending. Brightwell Lending helps customers get the right loan, whether its a home loan, investment loan, business loan etc.

You are required to come up with just the homepage design. Professionalism and quality is the key factors in the successful design.

Here are a few design questions to help you out:

-
What information should be used on the page?
Ive provided a document which outlines all the information needed to put on homepage (attached to the brief - called brightwell_page_info). Also see the Must Have section below on this brief.

-
What links should appear in the navigation/footer?:
The navigation should provide links to the following pages (NOTE: services link has subcategories):
1 Homepage
2 Services
- Home loans
- Investment loans
- Refinancing loans
- Business loans
3 About Us
4 FAQ
5 Contact Us

-
What colors should be used in the design?
Our company colors - Cyan: #2EADE3, Blue: #004B70, White. Feel free to submit designs with slight variations if you feel it improves the design.

-
What should the layout of the page be?
This is up to you to come up with - we are open to different layouts for the page design (as long as they capture the information effectively and making it easy to understand).

Target Market(s)

Potential Home owners, Families and Business Owners

Industry/Entity Type

Business

Requirements
Must have
• - Must contain our logo (attached as PNG and Illustrator file)
- Winning designer must supply a Photoshop file (PSD) that will allow us.
Nice to have
• - Should include photos/images of families, professional groups, tradespeople etc (you can use stock photos from PixQuarry and I will purchase them once you are selected as the winning design)
- Link to a loan calculator somewhere on front page with a button 'Find out how much you could borrow' (or maybe even try adding a loan calculator to the homepage if you think this would look good)
- Page should have a main headline "Finding the right loan for you" or "Brightwell Lending finds the right loan for our customers."
- Must include Accreditation logos somewhere on the homepage (will try and supply these soon)
Should not have
• - Poor quality designs will not be considered
- Do not use clipart

```html
<!DOCTYPE html>
<html lang="en">
<head>
<meta charset="utf-8">
<title>Brightwell Lending – Home</title>
<link rel="stylesheet" href="https://fonts.googleapis.com/css2?family=Arimo:wght@400;700&family=Roboto:wght@300;400&display=swap">
<style>
:root{
  --cyan:#2eade3;
  --blue:#004b70;
  --panel:#03486d;
  --ink:#333333;
  --link:#0b4b72;
  --rule:#222222;
  --dark:#2b2b2b;
  --soft:#dfeff8;
  --white:#ffffff;
  --border:#dddddd;
}
*{margin:0;padding:0;box-sizing:border-box}
html,body{width:1200px;height:1200px;overflow:hidden;background:var(--white)}
body{position:relative;font-family:"Arimo",Arial,sans-serif;color:var(--ink)}
.abs{position:absolute}
.sky{left:0;top:0}
.brand{left:130px;top:40px;display:flex;align-items:center;gap:10px;color:var(--cyan);font-size:20px;font-weight:700;letter-spacing:-0.3px}
.brand-dot{width:30px;height:30px;border-radius:50%;border:4px solid var(--cyan)}
.brand-rule{left:130px;top:99px;width:480px;height:2px;background:var(--cyan)}
.main-nav{left:659px;top:91px;display:flex;gap:0;font-size:12px;font-weight:700;color:var(--cyan);text-transform:uppercase}
.main-nav a{color:inherit;text-decoration:none}
.main-nav .sep{margin:0 18px;font-weight:400}
.hero{left:130px;top:120px;width:940px;height:240px;box-shadow:0 1px 4px rgba(0,0,0,.25)}
.hero-photo{left:0;top:0;width:360px;height:240px;background:linear-gradient(135deg,#b0723f 0%,#d9c3ab 35%,#9fbfd8 60%,#e8e2da 100%)}
.hero-panel{left:360px;top:0;width:580px;height:240px;background:var(--panel)}
.hero-title{left:38px;top:38px;width:460px;font-family:"Roboto",sans-serif;font-weight:300;font-size:30px;line-height:36px;color:var(--white)}
.hero-title svg{vertical-align:-4px;margin-left:10px}
.slider{left:478px;top:206px}
.rule{height:1px;background:var(--rule);top:390px}
.intro{left:130px;top:408px;width:620px;font-size:12px;line-height:14px}
.intro p{margin-bottom:8px}
.intro .name{color:var(--cyan);font-weight:700}
.intro .lead{color:var(--blue);font-weight:700}
.calc{left:770px;top:410px;width:300px;height:80px;background:repeating-linear-gradient(45deg,#2e2e2e 0 2px,#262626 2px 4px)}
.calc-icon{left:10px;top:14px}
.calc-text{left:79px;top:20px;font-size:14px;font-weight:700;line-height:17px;color:#eeeeee}
.service{top:540px;width:220px}
.service-head{height:36px;background:var(--blue);color:var(--white);font-size:14px;font-weight:700;display:flex;align-items:center;gap:8px;padding-left:10px}
.service ul{list-style:none;margin-top:11px}
.service li{font-size:12px;line-height:21px;color:var(--link);display:flex;align-items:center;gap:5px}
.service .sub{font-weight:700;color:var(--blue)}
.accred{left:130px;top:710px;width:940px;height:100px;border:1px solid var(--border)}
.accred-title{left:-1px;top:-1px;width:220px;height:100px;background:var(--cyan);color:var(--white);font-family:"Roboto",sans-serif;font-weight:300;font-size:18px;padding:16px 20px}
.accred-divider{top:10px;width:1px;height:80px;background:#e6e6e6}
.badge{top:33px;width:100px;height:26px;border-radius:4px;background:#d6d6d6}
.foot-rule{left:130px;top:900px;width:940px;height:2px;background:var(--cyan)}
.foot-links{left:130px;top:918px;font-size:11px;line-height:20px;color:var(--ink)}
.social{left:929px;top:920px;display:flex;gap:14px}
.social span{width:25px;height:25px;border-radius:50%;background:var(--cyan)}
</style>
</head>
<body>
<svg class="abs sky" width="1200" height="170" viewBox="0 0 1200 170" aria-hidden="true">
  <defs>
    <linearGradient id="skyFill" x1="0" y1="0" x2="0" y2="1">
      <stop offset="0" stop-color="#ffffff"/>
      <stop offset="1" stop-color="#bfe0f2"/>
    </linearGradient>
  </defs>
  <path d="M0 0H1200V120Q1120 140 1070 165V120H130V165Q80 140 0 120Z" fill="url(#skyFill)"/>
  <path d="M0 0H1200V90Q1000 115 600 115Q200 115 0 90Z" fill="#ffffff" opacity=".85"/>
</svg>

<header>
  <div class="abs brand"><span class="brand-dot"></span>brightwell lending</div>
  <div class="abs brand-rule"></div>
  <nav class="abs main-nav">
    <a href="#">Home</a><span class="sep">|</span>
    <a href="#">Services</a><span class="sep">|</span>
    <a href="#">About Us</a><span class="sep">|</span>
    <a href="#">FAQ</a><span class="sep">|</span>
    <a href="#">Contact Us</a>
  </nav>
</header>

<section class="abs hero">
  <div class="abs hero-photo" role="img" aria-label="Photo of a smiling couple meeting a loan adviser at home"></div>
  <div class="abs hero-panel">
    <h1 class="abs hero-title" style="font-weight:300">Brightwell Lending finds the right loan for our customers
      <svg width="24" height="24" viewBox="0 0 24 24" aria-hidden="true"><circle cx="12" cy="12" r="10.5" fill="none" stroke="#fff" stroke-width="2"/><path d="M6.5 12H17M12.5 7.5L17 12L12.5 16.5" fill="none" stroke="#fff" stroke-width="2"/></svg>
    </h1>
    <svg class="abs slider" width="76" height="16" viewBox="0 0 76 16" aria-hidden="true">
      <path d="M7 3L2 8L7 13" fill="none" stroke="#fff" stroke-width="2.5"/>
      <rect x="20" y="4" width="8" height="8" fill="#2eade3"/>
      <rect x="33" y="4" width="8" height="8" fill="#fff"/>
      <rect x="46" y="4" width="8" height="8" fill="#fff"/>
      <path d="M65 3L70 8L65 13" fill="none" stroke="#fff" stroke-width="2.5"/>
    </svg>
  </div>
</section>

<div class="abs rule" style="left:130px;width:620px"></div>
<div class="abs rule" style="left:770px;width:300px"></div>

<section class="abs intro">
  <p>At <span class="name">Brightwell Lending</span> we work hard to find the right loan for our customers. We do that because we are backed by sound industry knowledge, professional experience and a great customer service approach. Brightwell Lending guarantees that we will always tailor the best solution for your individual lending needs.</p>
  <p>We can do that because we have access to a wide variety of lending options from major banks to non-bank lenders and we are committed to finding the right lending product for you.</p>
  <p class="lead">We offer a unique approach to help you find the right:</p>
</section>

<a class="abs calc" href="#">
  <svg class="abs calc-icon" width="52" height="52" viewBox="0 0 52 52" aria-hidden="true">
    <circle cx="26" cy="26" r="25" fill="#3a3a3a" stroke="#bbb" stroke-width="2"/>
    <rect x="15" y="14" width="22" height="24" rx="2" fill="#ddd"/>
    <rect x="18" y="17" width="16" height="5" fill="#556"/>
    <g fill="#556"><rect x="18" y="25" width="4" height="3"/><rect x="24" y="25" width="4" height="3"/><rect x="30" y="25" width="4" height="3"/><rect x="18" y="30" width="4" height="3"/><rect x="24" y="30" width="4" height="3"/><rect x="30" y="30" width="4" height="3"/></g>
  </svg>
  <span class="abs calc-text">Find out how much you could<br>borrow &nbsp;&raquo;</span>
</a>

<section class="abs service" style="left:130px">
  <h2 class="service-head"><svg width="24" height="24" viewBox="0 0 24 24" aria-hidden="true"><circle cx="12" cy="12" r="11" fill="none" stroke="#fff" stroke-width="1.5"/><path d="M6 12L12 7L18 12V17H6Z" fill="#fff"/></svg>Home Loan</h2>
  <ul><li>&middot;&middot;&middot;&rsaquo; Home buyers</li><li>&middot;&middot;&middot;&rsaquo; First home buyers</li><li>&middot;&middot;&middot;&rsaquo; Over 20 lenders</li></ul>
</section>
<section class="abs service" style="left:370px">
  <h2 class="service-head"><svg width="24" height="24" viewBox="0 0 24 24" aria-hidden="true"><circle cx="12" cy="12" r="11" fill="none" stroke="#fff" stroke-width="1.5"/><rect x="6" y="11" width="5" height="6" fill="#fff"/><rect x="13" y="9" width="5" height="8" fill="#fff"/></svg>Investment Loan</h2>
  <ul><li>&middot;&middot;&middot;&rsaquo; Property investment loans</li><li>&middot;&middot;&middot;&rsaquo; Interest only loans</li></ul>
</section>
<section class="abs service" style="left:610px">
  <h2 class="service-head"><svg width="24" height="24" viewBox="0 0 24 24" aria-hidden="true"><circle cx="12" cy="12" r="11" fill="none" stroke="#fff" stroke-width="1.5"/><path d="M6 17L10 13L13 15L18 8" fill="none" stroke="#fff" stroke-width="2"/></svg>Refinancing</h2>
  <ul><li>&middot;&middot;&middot;&rsaquo; Refinancing for the best rate</li><li>&middot;&middot;&middot;&rsaquo; Upsizing or downsizing</li><li>&middot;&middot;&middot;&rsaquo; Change from a variable to a fixed rate</li></ul>
</section>
<section class="abs service" style="left:850px">
  <h2 class="service-head"><svg width="24" height="24" viewBox="0 0 24 24" aria-hidden="true"><circle cx="12" cy="12" r="11" fill="none" stroke="#fff" stroke-width="1.5"/><rect x="8" y="6" width="8" height="12" fill="none" stroke="#fff" stroke-width="1.5"/></svg>Business Loan</h2>
  <ul style="margin-top:11px"><li class="sub">Business Finance</li><li>&middot;&middot;&middot;&rsaquo; Long term</li><li>&middot;&middot;&middot;&rsaquo; Short term</li><li>&middot;&middot;&middot;&rsaquo; Equipment and Leasing</li></ul>
</section>

<section class="abs accred">
  <h2 class="abs accred-title" style="font-weight:300">Accreditation logos</h2>
  <div class="abs badge" style="left:299px"></div>
  <div class="abs accred-divider" style="left:470px"></div>
  <div class="abs badge" style="left:539px"></div>
  <div class="abs accred-divider" style="left:709px"></div>
  <div class="abs badge" style="left:774px"></div>
</section>

<footer>
  <div class="abs foot-rule"></div>
  <div class="abs foot-links">Terms of Use | Legal notice | Sitemap | Disclaimer<br>Copyright © 2012 Brightwell Lending.&nbsp; All rights reserved.</div>
  <div class="abs social"><span></span><span></span><span></span><span></span></div>
</footer>
</body>
</html>
```